Company Binded Folder Showcasing Services

We are wanting to create a presentation folder for potential customers seeking Concrete restoration, painting, waterproofing and more in Florida.
We would like presentation folder to have the following:
Color Scheme: Light or dark Gray, Black, Red, White (We are gravitating towards a darker color scheme)
Front of the folder and the back of the folder to have a symmetrical design with a large picture across (will send pictures as design goes on)
Front of folder should have logo, "25 years" logo, licensed and Insured with General Contractors number
Back of folder should have website, phone number, address, services/specialties listed

When the folder is opened...
The left side should have:
a pocket to put papers in
A business card insert

The right side should have tabs that are embedded in the folder. These tabs/sheets are going to be different sizes so titles along the edges can be visible (a picture can be sent for a visual)
We would like the tab colors to be red
Tab 1: Intro (Smallest Tab/Sheet)
Verbiage and pictures will be sent.
Tab 2: Railing Systems (Larger than tab 1)
Front and back of sheet used for small descriptions, testimonials and pictures.
Tab 3: Painting (Larger than Tab 2)
Verbiage and pictures will be sent
Tab 4: Concrete Restoration (Larger than Tab 3)
Tab 5: Waterproofing and Deck Systems (Largest Tab)
There will be a pocket on the right side of the folder to insert contracts/papers and another business card insert.

Target Market(s)

Property Managers, Building owners that have high rises, hospitality industrial or commercial buildings (especially near the ocean) along the coast of Florida. The company is located in Pompano Beach, but can travel.

Font styles to use
Other font styles liked:
• Match attached custom to complement logo

Colors
ec1f27

Requirements
Must have
• A clean, modern look.
• Pocket for sheets of paper and business card insert (on pocket) on both sides
• Embedded sheets into the folder that have titles along the edges with each sheet having different sizes to showcase services.
Nice to have
• Different designs for owner to choose from
• Darker color schemes
• Pictures edited if necessary to create a sharper image
Should not have
• No watermarks

```html
<!DOCTYPE html>
<html lang="en">
<head>
<meta charset="utf-8">
<title>Presentation Folder – Inside Spread</title>
<link rel="stylesheet" href="https://fonts.googleapis.com/css2?family=Barlow:wght@600;700&family=Open+Sans:wght@400;700&family=Tinos:wght@700&display=swap">
<style>
  :root{
    --red:#ec1f27;
    --red-deep:#9e1b2d;
    --red-mid:#c81f2c;
    --stage:#a3a3a3;
    --white:#ffffff;
    --photo-light:#f7f7f7;
    --photo-mid:#d9d9d9;
    --ink:#1a1a1a;
    --fold:#e2e2e2;
  }
  *{box-sizing:border-box;margin:0;padding:0}
  html,body{width:1200px;height:1200px;overflow:hidden}
  body{background:var(--stage);position:relative;font-family:"Open Sans",sans-serif}

  .spread{position:absolute;left:60px;top:250px;width:1080px;height:700px;display:flex;box-shadow:0 18px 40px rgba(0,0,0,.25)}
  .panel{position:relative;width:540px;height:700px;overflow:hidden;background:var(--white)}
  .panel--left{border-right:1px solid var(--fold)}

  .panel__photo{position:absolute;inset:0;background:linear-gradient(160deg,var(--photo-mid) 0%,var(--photo-light) 45%,#ececec 100%)}
  .panel--right .panel__photo{background:linear-gradient(200deg,var(--photo-light) 0%,#e6e6e6 55%,var(--photo-mid) 100%)}

  .corner-tab{position:absolute;left:0;top:0;width:110px;height:110px}

  .pocket{position:absolute;left:0;bottom:0;width:540px;height:230px;background:linear-gradient(180deg,var(--red) 0%,var(--red-mid) 55%,var(--red-deep) 100%);border-top-right-radius:26px}

  .card{position:absolute;left:160px;top:38px;width:270px;height:150px;background:linear-gradient(180deg,var(--red) 0%,var(--red-mid) 100%);overflow:hidden}
  .card__sweep{position:absolute;inset:0}
  .card__slit{position:absolute;width:40px;height:3px;background:var(--ink)}
  .card__slit--tl{left:-8px;top:28px;transform:rotate(-45deg)}
  .card__slit--br{right:-8px;bottom:26px;transform:rotate(-45deg)}
  .card__brand{position:absolute;left:92px;top:16px;width:170px;font-family:"Barlow",sans-serif;font-weight:700;font-size:15px;line-height:1.05;color:var(--red);text-align:center;text-transform:uppercase}
  .card__contact{position:absolute;left:118px;top:66px;list-style:none;font-family:"Tinos",serif;font-weight:700;font-size:8.5px;line-height:1.45;color:var(--ink)}
  .card__contact li{display:flex;align-items:center;gap:4px}
  .card__contact li:first-child{color:var(--red)}
  .card__contact svg{width:7px;height:7px;flex:none}
  .card__person{position:absolute;left:10px;bottom:10px;color:var(--white);font-size:7px;line-height:1.3}
  .card__name{font-size:11px;font-weight:700}
  .card__role{font-weight:400}
  .card__licence{font-weight:700}

  .tabs{position:absolute;right:0;top:0;width:250px;height:700px;background:linear-gradient(90deg,var(--red) 0%,var(--red) 45%,var(--red-deep) 100%)}
  .tab-title{position:absolute;top:34px;writing-mode:vertical-rl;font-family:"Barlow",sans-serif;font-weight:600;font-size:29px;letter-spacing:.5px;color:var(--white);text-transform:uppercase;white-space:nowrap}
  .tab-title--waterproofing{right:12px}
  .tab-title--concrete{right:58px}
  .tab-title--painting{right:104px}
  .tab-title--railing{right:150px}
  .tab-title--intro{right:196px}
</style>
</head>
<body>
  <main class="spread">
    <section class="panel panel--left">
      <div class="panel__photo" role="img" aria-label="Looking up along a glass office tower facade, light grey tones"></div>
      <svg class="corner-tab" viewBox="0 0 110 110" aria-hidden="true">
        <defs><linearGradient id="cornerRed" x1="0" y1="0" x2="1" y2="1"><stop offset="0" stop-color="#c81f2c"/><stop offset="1" stop-color="#ec1f27"/></linearGradient></defs>
        <polygon points="0,0 110,0 0,110" fill="url(#cornerRed)"/>
      </svg>
      <div class="pocket">
        <div class="card">
          <svg class="card__sweep" viewBox="0 0 270 150" preserveAspectRatio="none" aria-hidden="true">
            <path d="M60,0 L270,0 L270,150 L170,150 C110,120 70,60 60,0 Z" fill="#ffffff"/>
          </svg>
          <span class="card__slit card__slit--tl"></span>
          <span class="card__slit card__slit--br"></span>
          <div class="card__brand">Harlan's<br>Painting &amp; Restoration</div>
          <ul class="card__contact">
            <li><svg viewBox="0 0 10 10"><path d="M5 0a3.5 3.5 0 0 1 3.5 3.5C8.5 6 5 10 5 10S1.5 6 1.5 3.5A3.5 3.5 0 0 1 5 0z" fill="#ec1f27"/></svg>410 Harbor Ave Coral Bay FL 33000</li>
            <li><svg viewBox="0 0 10 10"><circle cx="5" cy="5" r="5" fill="#ec1f27"/></svg>555-201-4410</li>
            <li><svg viewBox="0 0 10 10"><circle cx="5" cy="5" r="5" fill="#ec1f27"/></svg>555-201-4477</li>
            <li><svg viewBox="0 0 10 10"><rect x="1" y="2" width="8" height="6" fill="#ec1f27"/></svg>harlansrestoration@mail.com</li>
            <li><svg viewBox="0 0 10 10"><circle cx="5" cy="5" r="4" fill="none" stroke="#ec1f27" stroke-width="1.5"/></svg>www.harlansrestoration.com</li>
          </ul>
          <div class="card__person">
            <div class="card__name">Daniel Marsh</div>
            <div class="card__role">Supervisor / Owner</div>
            <div class="card__licence">General Contractor<br>Licensed &amp; Insured<br>CGC7730412</div>
          </div>
        </div>
      </div>
    </section>

    <section class="panel panel--right">
      <div class="panel__photo" role="img" aria-label="Glass curtain wall of a high-rise seen from below, light grey tones"></div>
      <div class="tabs">
        <h2 class="tab-title tab-title--waterproofing">Waterproofing and Deck Systems</h2>
        <h2 class="tab-title tab-title--concrete">Concrete Restoration</h2>
        <h2 class="tab-title tab-title--painting">Painting</h2>
        <h2 class="tab-title tab-title--railing">Railing Systems</h2>
        <h2 class="tab-title tab-title--intro">Intro</h2>
      </div>
    </section>
  </main>
</body>
</html>
```